Fishing Tackle Store needs a gift box design

I need a contemporary design for the interior of a 'mystery' tackle gift box. We are a high end tackle store in Far North QLD, Australia called "Reefline Rod Cairns'. I have attached our logo for reference. Ideally I would like to include 3-5 fish facts (relative to our location and I can supply these) to give the gift boxes a point of difference, however I am really open to any creative design. Our main fish species are Barramundi, Tuna, Black Marlin, Giant Trevally, Sailfish, Wahoo, Spanish Mackerel. Colour - black / white. We are wanting these boxes to gain traction on social media so looking for an epic design! Thank you!

```html
<!DOCTYPE html>
<html lang="en">
<head>
<meta charset="utf-8">
<title>Reefline Rod Cairns – Spanish Mackerel Gift Box Insert</title>
<link rel="stylesheet" href="https://fonts.googleapis.com/css2?family=Anton&family=Source+Sans+3:wght@400;500&display=swap">
<style>
  :root {
    --ink: #000000;
    --paper: #ffffff;
    --rule: #bdbdbd;
    --stage: #2a2a2a;
    --fish-light: #d9d9d9;
    --fish-mid: #8a8a8a;
    --fish-dark: #2e2e2e;
  }
  * { margin: 0; padding: 0; box-sizing: border-box; }
  html, body { width: 1200px; height: 504px; overflow: hidden; background: var(--stage); }
  .insert {
    position: absolute; left: 279px; top: 0;
    width: 641px; height: 504px;
    background: var(--ink); color: var(--paper);
    font-family: "Source Sans 3", sans-serif;
  }
  .frame-outer, .frame-inner { position: absolute; border: 1px solid var(--rule); }
  .frame-outer { left: 24px; top: 27px; right: 25px; bottom: 26px; }
  .frame-inner { left: 28px; top: 31px; right: 29px; bottom: 30px; opacity: .6; }
  .size-badge {
    position: absolute; width: 166px; height: 166px; border-radius: 50%;
    border: 1.5px solid var(--paper); background: var(--ink);
    display: flex; flex-direction: column; align-items: center; justify-content: center;
    text-align: center;
  }
  .size-badge--average { left: 12px; top: 54px; }
  .size-badge--trophy { left: 463px; top: 54px; }
  .size-badge__label { font-size: 8.5px; letter-spacing: 1.6px; font-weight: 500; margin-bottom: 2px; }
  .size-badge__value { font-family: "Anton", sans-serif; font-size: 62px; line-height: 0.95; }
  .size-badge__unit { font-family: "Anton", sans-serif; font-size: 21px; line-height: 1.1; }
  .title {
    position: absolute; left: 200px; top: 52px; width: 242px;
    font-family: "Anton", sans-serif; font-weight: 400;
    font-size: 50px; line-height: 1.02; text-align: center; letter-spacing: .5px;
  }
  .fish-art {
    position: absolute; left: 44px; top: 186px; width: 552px; height: 150px;
    border-radius: 50% 20% 20% 50% / 50% 40% 40% 50%;
    background: radial-gradient(ellipse at 45% 50%, var(--fish-light) 0%, var(--fish-mid) 55%, var(--fish-dark) 85%, var(--ink) 100%);
    opacity: .85;
  }
  .facts { position: absolute; left: 51px; top: 352px; right: 40px; }
  .fact { position: absolute; top: 0; width: 170px; }
  .fact--one { left: 0; }
  .fact--two { left: 202px; }
  .fact--three { left: 397px; }
  .fact__heading { font-family: "Anton", sans-serif; font-weight: 400; font-size: 32px; line-height: 1.08; }
  .fact__body { margin-top: 12px; font-size: 9.2px; line-height: 1.75; }
  .divider { position: absolute; top: 365px; width: 0; height: 88px; border-left: 1px solid var(--rule); }
  .divider--one { left: 226px; }
  .divider--two { left: 418px; }
</style>
</head>
<body>
  <main class="insert">
    <div class="frame-outer"></div>
    <div class="frame-inner"></div>

    <div class="fish-art" role="img" aria-label="Detailed black and white engraved illustration of a Spanish mackerel swimming left"></div>

    <div class="size-badge size-badge--average">
      <span class="size-badge__label">AVERAGE SIZE</span>
      <span class="size-badge__value">16</span>
      <span class="size-badge__unit">INCHES</span>
    </div>

    <h1 class="title">SPANISH<br>MACKEREL</h1>

    <div class="size-badge size-badge--trophy">
      <span class="size-badge__label">TROPHY SIZE</span>
      <span class="size-badge__value">26</span>
      <span class="size-badge__unit">INCHES</span>
    </div>

    <section class="facts">
      <article class="fact fact--one">
        <h2 class="fact__heading">ANOTHER<br>FISH FACT</h2>
        <p class="fact__body">Fish fact listed here. Interesting fact<br>about the Spanish Mackerel.</p>
      </article>
      <article class="fact fact--two">
        <h2 class="fact__heading">FISH TYPE<br>FACTORS</h2>
        <p class="fact__body">Fish fact listed here. Interesting fact<br>about the Spanish Mackerel.</p>
      </article>
      <article class="fact fact--three">
        <h2 class="fact__heading">FISHING<br>FACTS</h2>
        <p class="fact__body">Fish fact listed here. Interesting fact<br>about the Spanish Mackerel.</p>
      </article>
    </section>
    <div class="divider divider--one"></div>
    <div class="divider divider--two"></div>
  </main>
</body>
</html>
```